Varnath Consulting Business card design.

See our website www.varnathconsulting-example.com which will give you a good idea of what we are about. The font is called 'Play'.

I'd like a standout business card in keeping with the themes and branding on the website

Target Market(s)

professionals. HR directors

Industry/Entity Type

Business

Contact Information for Business Card

Varnath Consulting PO Box 3917 Tindale Creek NSW 2840 1300 457 318 Gerald Ashbury Principal email: jobs@varnathconsulting-example.com ABN: 31792048663

Font styles to use
Other font styles liked:
• Play

Requirements
Must have
• Must have same design colours and branding as website.
• On back I'd prefer a list of the things we do which appears below the name at the header on the website

```html
<!DOCTYPE html>
<html lang="en">
<head>
<meta charset="utf-8">
<title>Varnath Consulting – Business Card</title>
<link rel="stylesheet" href="https://fonts.googleapis.com/css2?family=Play:wght@400;700&display=swap">
<style>
  :root {
    --navy: #0d2135;
    --blue: #3a93d3;
    --white: #ffffff;
    --page: #ffffff;
    --card-edge: #d6d6d6;
  }
  * { margin: 0; padding: 0; box-sizing: border-box; }
  html, body {
    width: 1200px;
    height: 1000px;
    overflow: hidden;
    background: var(--page);
    font-family: 'Play', sans-serif;
  }
  .canvas { position: relative; width: 1200px; height: 1000px; }

  .card {
    position: absolute;
    left: 326px;
    width: 548px;
    height: 338px;
  }
  .card--front { top: 143px; background: var(--navy); }
  .card--back { top: 518px; background: var(--white); border: 1px solid var(--card-edge); }

  .brand-name {
    position: absolute;
    top: 131px;
    left: 0;
    width: 100%;
    text-align: center;
    font-size: 42px;
    line-height: 1;
    font-weight: 400;
    color: var(--white);
    letter-spacing: 0.3px;
  }
  .services {
    position: absolute;
    top: 185px;
    left: 0;
    width: 100%;
    text-align: center;
    font-size: 12.5px;
    line-height: 1;
    color: var(--blue);
    letter-spacing: 0.9px;
  }
  .services .sep { color: var(--white); margin: 0 3px; }

  .contact {
    position: absolute;
    right: 48px;
    text-align: right;
    color: var(--blue);
    line-height: 1;
    white-space: nowrap;
  }
  .contact__name { top: 66px; font-size: 19px; letter-spacing: 1px; }
  .contact__phone {
    top: 90px;
    font-size: 58px;
    display: flex;
    align-items: center;
    gap: 4px;
  }
  .contact__phone svg { width: 44px; height: 46px; }
  .contact__email { top: 151px; font-size: 19px; letter-spacing: 0.5px; }

  .postal {
    position: absolute;
    left: 56px;
    top: 214px;
    color: var(--navy);
    line-height: 1;
  }
  .postal__company { font-size: 19px; margin-bottom: 5px; }
  .postal__line { font-size: 13.5px; line-height: 16px; letter-spacing: 0.3px; }
</style>
</head>
<body>
<div class="canvas">

  <section class="card card--front">
    <h1 class="brand-name">VARNATH CONSULTING</h1>
    <p class="services">
      Search &amp; Select<span class="sep">I</span>Career<span class="sep">I</span>Coaching<span class="sep">I</span>Leadership<span class="sep">I</span>Outplacement
    </p>
  </section>

  <section class="card card--back">
    <p class="contact contact__name">GERALD ASHBURY</p>
    <p class="contact contact__phone">
      <svg viewBox="0 0 24 24" aria-hidden="true">
        <path fill="#0d2135" d="M6.6 10.8c1.4 2.8 3.8 5.1 6.6 6.6l2.2-2.2c.3-.3.7-.4 1-.2 1.1.4 2.3.6 3.6.6.6 0 1 .4 1 1V20c0 .6-.4 1-1 1C10.6 21 3 13.4 3 4c0-.6.4-1 1-1h3.5c.6 0 1 .4 1 1 0 1.3.2 2.5.6 3.6.1.3 0 .7-.2 1z"/>
      </svg>
      1300 457 318
    </p>
    <p class="contact contact__email">jobs@varnathconsulting-example.com</p>

    <address class="postal" style="font-style:normal">
      <p class="postal__company">VARNATH CONSULTING</p>
      <p class="postal__line">PO Box 3917</p>
      <p class="postal__line">Tindale Creek NSW 2840</p>
      <p class="postal__line">www.varnathconsulting-example.com</p>
    </address>
  </section>

</div>
</body>
</html>
```